Flyer-Design für Anbieter von hochwertigem Futter für Kaninchen
Zielgruppe
Wir bieten hochwertiges Futter (Hauptfutter wie Heu aus eigener Herstellung aber auch Zusatzfutter) für Kaninchen.
Unsere Zielgruppe sind laut Auswertung unsers Online-Shops hauptsächlich weibliche Kunden (82%) und im Durchschnitt 40 Jahre alt.
Aufgabenstellung
Allgemeines:
- Flyer soll als Werbemedium gestaltet werden
- Design im Querformat DinA5
Inhalte:
- Logo Grasbündel.de
- www. grasbündel.de
- Kunden bewerten mit 'sehr gut'
- Familienbetrieb seit über 100 Jahren
- Geprüftes Qualitätsheu aus der Eifel
- frischer, aromatischer Heuduft von naturbelassenen, grünen Eifelwiesen
- Heu, Stroh und viele weitere Produkte im Shop
- Ökologische Papier-Verpackung
- Schneller und kostengünstiger Versand
Zusatzinfos:
- Die Datei normalheupng.png kann als Logo verwendet werden
- Als Idee könnte evt. auch ein Bild 89328394.jpg (Eifellandschaft Heuernte) in irgendweiner Form integriert werden.
- Folgende Bilddateien wurden über Bildaro gekauft:
- Es können bei Bedarf auch Kosten für weitere Bilder erworben werden

```html
<!DOCTYPE html>
<html lang="de">
<head>
<meta charset="utf-8">
<title>Grasbündel Flyer</title>
<link rel="stylesheet" href="https://fonts.googleapis.com/css2?family=Arimo:wght@400;700&display=swap">
<style>
  :root {
    --stage: #5b5b5d;
    --cream: #f7f3a9;
    --ink: #2b2b2b;
    --sun: #fde034;
    --amber: #fdab05;
    --orange: #f0a020;
    --white: #ffffff;
  }
  html, body {
    margin: 0;
    width: 1200px;
    height: 1200px;
    overflow: hidden;
    background: var(--stage);
    font-family: "Arimo", Arial, sans-serif;
  }
  .flyer {
    position: absolute;
    left: 50px;
    top: 211px;
    width: 1100px;
    height: 777px;
    display: block;
  }
  .flyer text { font-family: "Arimo", Arial, sans-serif; }
  .brand-name { font-size: 46px; font-weight: 700; fill: var(--ink); }
  .tagline { font-size: 17px; font-weight: 700; fill: var(--ink); }
  .intro { font-size: 21px; font-weight: 700; fill: var(--ink); }
  .benefit { font-size: 23px; fill: var(--ink); }
  .service { font-size: 18px; font-weight: 700; fill: var(--ink); }
  .contact-small { font-size: 21px; fill: var(--white); }
  .phone { font-size: 40px; font-weight: 700; fill: var(--white); }
  .address { font-size: 26px; fill: var(--white); }
  .address-bold { font-weight: 700; }
  .tick { fill: none; stroke: var(--ink); stroke-width: 3.5; stroke-linecap: round; stroke-linejoin: round; }
  .tick-small { fill: none; stroke: var(--ink); stroke-width: 2.5; stroke-linecap: round; stroke-linejoin: round; }
</style>
</head>
<body>
<svg class="flyer" viewBox="0 0 1210 855" xmlns="http://www.w3.org/2000/svg">
  <defs>
    <linearGradient id="sunToAmber" x1="0" y1="0" x2="1" y2="0">
      <stop offset="0" stop-color="var(--sun)"/>
      <stop offset="1" stop-color="var(--amber)"/>
    </linearGradient>
    <linearGradient id="amberToSun" x1="0" y1="0" x2="1" y2="0">
      <stop offset="0" stop-color="var(--amber)"/>
      <stop offset="1" stop-color="var(--sun)"/>
    </linearGradient>
    <linearGradient id="fieldTones" x1="0" y1="0" x2="0" y2="1">
      <stop offset="0" stop-color="#c9c7a6"/>
      <stop offset="0.3" stop-color="#7f9a3e"/>
      <stop offset="1" stop-color="#a8a150"/>
    </linearGradient>
    <linearGradient id="rabbitTones" x1="0" y1="0" x2="0" y2="1">
      <stop offset="0" stop-color="#f4f2ee"/>
      <stop offset="0.6" stop-color="#8a7a6a"/>
      <stop offset="1" stop-color="#5f8a3a"/>
    </linearGradient>
    <linearGradient id="carrotTones" x1="0" y1="0" x2="1" y2="1">
      <stop offset="0" stop-color="#f1d7b4"/>
      <stop offset="1" stop-color="#e8742a"/>
    </linearGradient>
  </defs>

  <rect class="flyer-ground" width="1210" height="855" fill="var(--cream)"/>

  <!-- top banner triangle -->
  <polygon points="577,0 939,0 757,182" fill="url(#sunToAmber)"/>

  <!-- landscape panel -->
  <polygon role="img" aria-label="Foto: Eifellandschaft mit Heuballen auf der Wiese"
           points="939,0 1089,0 1210,138 1210,410 1026,565 714,242 939,0" fill="url(#fieldTones)"/>
  <polygon points="1119,80 1210,170 1210,350 1119,430 948,252" fill="var(--amber)" opacity="0.45"/>

  <!-- rabbit panel -->
  <polygon role="img" aria-label="Foto: Kaninchen im Gras"
           points="582,47 737,202 582,354 427,202" fill="url(#rabbitTones)"/>
  <polygon points="507,95 614,202 507,309 400,202" fill="var(--orange)" opacity="0.85"/>

  <!-- hay panel -->
  <polygon role="img" aria-label="Foto: Nahaufnahme von Heu"
           points="704,265 809,370 704,475 599,370" fill="#c8c9bf"/>

  <!-- small accent diamond -->
  <polygon points="824,382 897,455 824,528 751,455" fill="url(#sunToAmber)"/>

  <!-- carrot panel -->
  <polygon points="1107,512 1210,410 1210,437 1122,526" fill="var(--amber)"/>
  <polygon role="img" aria-label="Foto: Kaninchen mit Karotten"
           points="1054,590 1210,437 1210,746" fill="url(#carrotTones)"/>

  <!-- bottom right banner -->
  <polygon points="742,668 1210,668 1210,855 929,855" fill="url(#sunToAmber)"/>
  <polygon points="765,829 847,722 927,829" fill="url(#sunToAmber)"/>

  <!-- bottom left band -->
  <polygon points="0,761 540,761 632,855 0,855" fill="url(#amberToSun)"/>

  <!-- brand -->
  <g class="brand">
    <circle cx="180" cy="170" r="62" fill="var(--orange)"/>
    <text class="brand-name" x="180" y="300" text-anchor="middle">Grasbündel</text>
    <text class="tagline" x="180" y="336" text-anchor="middle">Familienbetrieb seit über 100 Jahren</text>
    <text class="tagline" x="180" y="360" text-anchor="middle">Kunden bewerten mit ‚sehr gut‘</text>
  </g>

  <!-- benefits -->
  <g class="benefits">
    <text class="intro" x="99" y="413">Warum unser Heu bei unseren Kunden bzw.</text>
    <text class="intro" x="99" y="441">Ihren kleinen Lieblingen so gut ankommt:</text>

    <path class="tick" d="M55,477 l6,8 l11,-17"/>
    <text class="benefit" x="99" y="479">enthält wenige Kräuter und wirkt sich positiv auf die</text>
    <text class="benefit" x="99" y="508">gesunde Ernährung aus</text>

    <path class="tick" d="M55,535 l6,8 l11,-17"/>
    <text class="benefit" x="99" y="536">lange Halme dienen der optimalen Unterstützung</text>
    <text class="benefit" x="99" y="565">des Zahnabriebs</text>

    <path class="tick" d="M55,591 l6,8 l11,-17"/>
    <text class="benefit" x="99" y="593">verbessert die Verdauung und daher gut verträglich</text>
    <text class="benefit" x="99" y="622">für Kleintiere</text>

    <path class="tick" d="M55,649 l6,8 l11,-17"/>
    <text class="benefit" x="99" y="651">als Streu angenehm wärmend</text>

    <path class="tick" d="M55,677 l6,8 l11,-17"/>
    <text class="benefit" x="99" y="679">frischer, aromatischer Heuduft von grünen Eifelwiesen</text>

    <path class="tick" d="M55,706 l6,8 l11,-17"/>
    <text class="benefit" x="99" y="708">nährstoffreiche, leckere, gesunde Gräser</text>
  </g>

  <!-- service points -->
  <g class="services">
    <path class="tick-small" d="M652,582 l4,6 l8,-12"/>
    <text class="service" x="672" y="588">Geprüftes Qualitätsheu aus der Eifel</text>
    <path class="tick-small" d="M652,605 l4,6 l8,-12"/>
    <text class="service" x="672" y="611">Heu, Stroh und viele weitere Produkte</text>
    <path class="tick-small" d="M652,628 l4,6 l8,-12"/>
    <text class="service" x="672" y="634">Ökologische Papier-Verpackung</text>
    <path class="tick-small" d="M652,651 l4,6 l8,-12"/>
    <text class="service" x="672" y="657">Schneller, günstiger Versand</text>
  </g>

  <!-- contact left -->
  <text class="contact-small" x="42" y="802">mail@grasbuendel.de</text>
  <text class="contact-small" x="44" y="829">www.grasbündel.de</text>
  <text class="phone" x="326" y="830">02345-6789</text>

  <!-- address right -->
  <text class="address" x="938" y="721">Grasbuendel.de</text>
  <text class="address address-bold" x="938" y="753">M. HOLLBACH</text>
  <text class="address" x="938" y="786">Lindenweg 14</text>
  <text class="address" x="938" y="818">54321 Wiesental</text>
</svg>
</body>
</html>
```